I want a double sided flyer possibly with a picture of a lawn or grass.
Company name, phone number, email, and logo
Corvane Lawn Management, (404)672-8154,Corvane_Lawn@brisknet.com
Company services
Fertilization and weed control,Lawn and Landscape maintenance, mowing, pruning, aeration, landscape and Christmas lights,

```html
<!DOCTYPE html>
<html lang="en">
<head>
<meta charset="utf-8">
<title>Corvane Lawn Management – Flyer</title>
<link rel="stylesheet" href="https://fonts.googleapis.com/css2?family=Lato:wght@400;700;900&display=swap">
<style>
  :root {
    --grass-light: #8fdc2c;
    --grass-mid: #4fb81a;
    --grass-deep: #2d7d0e;
    --rule: #2b5e12;
    --badge-red: #e8262b;
    --ink: #111111;
    --white: #ffffff;
    --outline: #1d3a0a;
  }
  * { box-sizing: border-box; margin: 0; padding: 0; }
  html, body { width: 927px; height: 1200px; overflow: hidden; background: var(--white); }
  body { font-family: "Lato", Arial, sans-serif; }

  .flyer { position: relative; width: 927px; height: 1200px; overflow: hidden; }

  .grass-backdrop {
    position: absolute; inset: 0;
    background:
      radial-gradient(ellipse at 30% 20%, rgba(190,240,90,.55), transparent 55%),
      radial-gradient(ellipse at 75% 70%, rgba(170,235,70,.5), transparent 55%),
      repeating-linear-gradient(100deg, rgba(40,110,10,.18) 0 6px, transparent 6px 22px),
      linear-gradient(180deg, var(--grass-light), var(--grass-mid) 45%, var(--grass-light) 55%, var(--grass-mid) 80%, var(--grass-deep));
  }

  .rule { position: absolute; height: 4px; background: var(--rule); }
  .rule--top { left: 27px; right: 7px; top: 147px; }
  .rule--fold { left: 0; right: 0; top: 560px; }

  .brand-name {
    position: absolute; color: var(--ink); font-weight: 900; line-height: 1;
  }
  .brand-name--front { left: 77px; top: 180px; font-size: 40px; }
  .brand-name--front span { display: block; font-size: 26px; margin-top: 6px; }
  .brand-name--back { left: 0; right: 0; top: 880px; text-align: center; font-size: 110px; }
  .brand-name--back span { display: block; font-size: 56px; margin-top: 14px; }

  .outlined {
    color: var(--white); font-weight: 700;
    text-shadow: -1px -1px 0 var(--outline), 1px -1px 0 var(--outline), -1px 1px 0 var(--outline), 1px 1px 0 var(--outline), 0 2px 3px rgba(0,0,0,.4);
  }

  .services-heading { position: absolute; left: 420px; top: 101px; font-size: 27px; letter-spacing: .2px; }

  .contact-prompt { position: absolute; left: 27px; top: 338px; font-size: 24px; }

  .badge {
    position: absolute; width: 72px; height: 72px; border-radius: 50%;
    background: var(--badge-red); display: flex; align-items: center; justify-content: center;
    box-shadow: 0 1px 3px rgba(0,0,0,.3);
  }
  .badge--small { width: 58px; height: 58px; }
  .badge svg { width: 60%; height: 60%; }

  .service-label, .contact-value { position: absolute; white-space: nowrap; }
  .service-label { font-size: 23px; transform: translateY(-50%); }
  .contact-value { font-size: 18px; transform: translateY(-50%); }
</style>
</head>
<body>
<main class="flyer">
  <div class="grass-backdrop" role="img" aria-label="Close-up photograph of fresh green lawn grass filling both sides of the flyer"></div>

  <!-- Front side -->
  <section class="side side--front">
    <div class="brand-name brand-name--front">Corvane<span>Lawn Management</span></div>

    <h2 class="services-heading outlined">WE PROVIDE FOLLOWING SERVICES</h2>
    <div class="rule rule--top"></div>

    <div class="badge" style="left:400px;top:168px">
      <svg viewBox="0 0 40 40" fill="#fff"><rect x="8" y="16" width="18" height="8" rx="2" transform="rotate(-40 17 20)"/><rect x="20" y="6" width="6" height="16" rx="2" transform="rotate(-40 23 14)"/></svg>
    </div>
    <div class="service-label outlined" style="left:487px;top:204px">Pruning</div>

    <div class="badge" style="left:627px;top:168px">
      <svg viewBox="0 0 40 40" fill="#fff"><rect x="8" y="18" width="24" height="10" rx="2"/><rect x="22" y="8" width="3" height="12" transform="rotate(25 23 14)"/><circle cx="12" cy="30" r="4"/><circle cx="28" cy="30" r="4"/></svg>
    </div>
    <div class="service-label outlined" style="left:711px;top:204px">Mowing</div>

    <div class="badge" style="left:400px;top:268px">
      <svg viewBox="0 0 40 40" fill="#fff"><rect x="6" y="20" width="28" height="12" rx="2"/><path d="M18 18c0-7 6-10 10-10-1 6-4 10-10 10z"/></svg>
    </div>
    <div class="service-label outlined" style="left:487px;top:304px">Aeration</div>

    <div class="badge" style="left:627px;top:268px">
      <svg viewBox="0 0 40 40" fill="#fff"><path d="M20 4l6 9h-3l6 8h-3l6 9H8l6-9h-3l6-8h-3z"/><rect x="18" y="30" width="4" height="6"/></svg>
    </div>
    <div class="service-label outlined" style="left:711px;top:304px">Christmas lights</div>

    <div class="badge" style="left:400px;top:374px">
      <svg viewBox="0 0 40 40" fill="#fff"><rect x="12" y="16" width="14" height="20" rx="4"/><rect x="14" y="8" width="8" height="8"/><rect x="22" y="9" width="6" height="3"/><circle cx="32" cy="8" r="1.3"/><circle cx="34" cy="12" r="1.3"/><circle cx="31" cy="14" r="1.3"/></svg>
    </div>
    <div class="service-label outlined" style="left:487px;top:410px">Fertilization, Weed Control</div>

    <div class="badge" style="left:400px;top:474px">
      <svg viewBox="0 0 40 40" fill="#fff"><path d="M4 30c8-6 24-6 32 0v4H4z"/><rect x="18" y="6" width="3" height="18" transform="rotate(20 19 15)"/><path d="M14 22l8 2-3 8-6-3z"/></svg>
    </div>
    <div class="service-label outlined" style="left:487px;top:510px">Lawn and Landscape maintenance</div>

    <p class="contact-prompt outlined">Call today or send an email</p>

    <div class="badge badge--small" style="left:31px;top:398px">
      <svg viewBox="0 0 40 40"><text x="20" y="29" text-anchor="middle" font-family="Lato, Arial, sans-serif" font-weight="700" font-size="28" fill="#fff">@</text></svg>
    </div>
    <div class="contact-value outlined" style="left:107px;top:425px">Corvane_Lawn@brisknet.com</div>

    <div class="badge badge--small" style="left:31px;top:482px">
      <svg viewBox="0 0 40 40" fill="#fff"><path d="M12 6l5 7-3 3c2 4 5 7 9 9l3-3 7 5-3 5C19 36 4 21 7 9z"/></svg>
    </div>
    <div class="contact-value outlined" style="left:109px;top:511px">(404)672-8154</div>

    <div class="rule rule--fold"></div>
  </section>

  <!-- Back side -->
  <section class="side side--back">
    <div class="brand-name brand-name--back">Corvane<span>Lawn Management</span></div>
  </section>
</main>
</body>
</html>
```